IG ad to attract older men for better health #1

I want a bold headline Instagram Ad that coordinate with my website design with a racy sexy woman to attract men 45yrs old plus. See Two samples attached

Target Market(s)

Men 45 years old and older

Industry/Entity Type

Health And Wellness

Requirements
Must have
• eye catching appeal to men
Nice to have
• The copy to read
Kestrel61go is the headline at the top of the page. Then the copy reads...
"I want to seduce you to better health with a little T&A. Remove the excuses, provide ridiculously simple tips and advice to get you started on a path of lasting heath." Want more?

```html
<!DOCTYPE html>
<html lang="en">
<head>
<meta charset="utf-8">
<title>Kestrel61go Instagram Ads</title>
<link href="https://fonts.googleapis.com/css2?family=Montserrat:ital,wght@0,500;0,600;0,800;1,800&display=swap" rel="stylesheet">
<style>
  :root {
    --page: #f4f4f4;
    --ink: #111518;
    --navy-panel: #0f1a20;
    --pool-light: #5cc6ec;
    --pool-deep: #1a8fd0;
    --ring-navy: #0c4676;
    --sand-light: #e9d3b8;
    --sand-deep: #b98a62;
    --skin-warm: #8a5a3c;
    --peach: #f3a46c;
    --orange: #e8843f;
  }
  * { box-sizing: border-box; margin: 0; padding: 0; }
  html, body {
    width: 1200px; height: 941px; overflow: hidden;
    background: var(--page);
    font-family: "Montserrat", sans-serif;
  }
  .ad-row {
    position: absolute; top: 200px; left: 40px;
    display: flex; gap: 40px;
  }
  .ad {
    position: relative; width: 540px; height: 540px; overflow: hidden;
  }
  .ad-photo { position: absolute; inset: 0; }
  .ad--pool .ad-photo {
    background: radial-gradient(circle at 30% 45%, #d9a483 0 18%, transparent 34%),
                linear-gradient(160deg, var(--pool-light), var(--pool-deep));
  }
  .ad--beach .ad-photo {
    background: radial-gradient(ellipse at 30% 55%, var(--skin-warm) 0 18%, transparent 42%),
                linear-gradient(170deg, #f3ece3 0%, var(--sand-light) 35%, var(--sand-deep) 100%);
  }
  .ad-shapes { position: absolute; inset: 0; width: 540px; height: 540px; }
  .headline {
    position: absolute; font-weight: 800; letter-spacing: -0.5px; line-height: 1;
    white-space: nowrap;
  }
  .ad--pool .headline { right: 30px; top: 30px; font-size: 42px; color: var(--peach); }
  .ad--beach .headline { right: 30px; top: 66px; font-size: 42px; color: var(--ink); }
  .quote {
    position: absolute; text-align: right; color: var(--peach);
    font-weight: 600; white-space: nowrap;
  }
  .ad--pool .quote { right: 32px; top: 104px; font-size: 17px; line-height: 21.4px; }
  .ad--beach .quote { right: 20px; top: 186px; font-size: 16px; line-height: 20.3px; }
  .cta {
    position: absolute; height: 28px; z-index: 1; isolation: isolate;
    display: flex; align-items: center; justify-content: center;
    font-weight: 800; font-style: italic; font-size: 17px; color: var(--ink);
  }
  .cta::before {
    content: ""; position: absolute; inset: 0; z-index: -1;
    background: var(--orange); transform: skewX(-20deg);
  }
  .ad--pool .cta { right: 18px; top: 289px; width: 148px; }
  .ad--pool .cta::before { background: var(--peach); }
  .ad--beach .cta { right: 20px; top: 413px; width: 148px; }
</style>
</head>
<body>
<main class="ad-row">

  <section class="ad ad--pool">
    <div class="ad-photo" role="img" aria-label="Photo of a smiling woman in a dark bikini and sunglasses climbing out of a blue swimming pool by a steel ladder"></div>
    <svg class="ad-shapes" viewBox="0 0 540 540" aria-hidden="true">
      <path d="M205 0 H540 V352 C480 318 320 330 262 395 C262 300 275 140 205 0 Z" fill="var(--navy-panel)"/>
      <path d="M205 0 C275 140 262 300 262 395" fill="none" stroke="var(--ring-navy)" stroke-width="12"/>
      <path d="M262 395 C320 330 480 318 540 352 V540 H262 Z" fill="var(--pool-deep)" opacity="0.55"/>
      <path d="M262 395 C320 330 480 318 540 352" fill="none" stroke="var(--ring-navy)" stroke-width="12"/>
      <circle cx="0" cy="0" r="26" fill="none" stroke="var(--ring-navy)" stroke-width="8"/>
      <circle cx="24" cy="75" r="9" fill="var(--ring-navy)"/>
      <circle cx="498" cy="426" r="12" fill="var(--ring-navy)"/>
      <circle cx="510" cy="540" r="28" fill="none" stroke="var(--ring-navy)" stroke-width="8"/>
    </svg>
    <h2 class="headline">Kestrel61go</h2>
    <p class="quote">"I want to seduce you<br>to better health with a<br>little T&amp;A. Remove the<br>excuses, provide<br>ridiculously simple tips<br>and advice to get you<br>started on a path of<br>lasting health."</p>
    <span class="cta">Want more?</span>
  </section>

  <section class="ad ad--beach">
    <div class="ad-photo" role="img" aria-label="Photo of a tanned woman with long dark hair in a black bikini kneeling in the surf on a sandy beach"></div>
    <svg class="ad-shapes" viewBox="0 0 540 540" aria-hidden="true">
      <polygon points="0,0 33,0 33,62 0,45" fill="var(--ink)"/>
      <rect x="455" y="0" width="85" height="33" fill="var(--orange)"/>
      <rect x="270" y="215" width="30" height="55" fill="var(--orange)"/>
      <polygon points="244,152 540,152 540,388 345,388" fill="var(--navy-panel)"/>
      <rect x="0" y="506" width="33" height="34" fill="var(--orange)"/>
      <rect x="509" y="480" width="31" height="60" fill="var(--ink)"/>
    </svg>
    <h2 class="headline">Kestrel61go</h2>
    <p class="quote">"I want to seduce you<br>to better health with a<br>little T&amp;A. Remove the<br>excuses, provide<br>ridiculously simple tips<br>and advice to get you<br>started on a path of<br>lasting health."</p>
    <span class="cta">Want more?</span>
  </section>

</main>
</body>
</html>
```